New website design for small car detailing company.

We have a small cleaning company, our main focus is car detailing but we are also expanding to home and residential cleaning and power washing.
I would like the web site to have a simple layout and SEO friendly.
I would also like to have a contact page in which clients can contact us and upload pictures of the house or car so we can provide an estimate.
A Page that shows the services we offer.

Target Market(s)

High paying clients for car detailiing and focus on residential and commercial cleaning.

Industry/Entity Type

Cleaning Service

Coding

Coded - Design and coding required

Number of Pages Required

4 page

Font styles to use
Serif

Colors

Designer to choose only greyscale colors for use in the design.

Requirements
Must have
• A home page.
Blog page for SEO
Contact page with the choice of clients to upload theirs pictures so we can provide estimates with calendar integration so they can provide their available dates for service.
A pictures to sell our services.
Nice to have
• Simple but sleek desing, I am more interested in SEO Score than heavy loads

```html
<!DOCTYPE html>
<html lang="en">
<head>
<meta charset="utf-8">
<title>Shoreline Mobile Detailing – Interior and Exterior Cleaning</title>
<link href="https://fonts.googleapis.com/css2?family=Playfair+Display:wght@600;700&family=Crimson+Pro:wght@400;600&display=swap" rel="stylesheet">
<style>
:root{
  --black:#111;
  --ink:#1c1c1c;
  --accent:#4a4a4a;
  --accent-light:#c4c4c4;
  --band:#2e2e2e;
  --dark:#262626;
  --darker:#161616;
  --white:#fff;
  --light:#efefef;
  --line:#8a8a8a;
}
*{box-sizing:border-box;margin:0;padding:0}
html,body{width:1200px;height:2503px;overflow:hidden}
body{position:relative;font-family:"Crimson Pro",serif;color:var(--ink);background:var(--white)}
.abs{position:absolute}
.heading{font-family:"Playfair Display",serif;font-weight:700}
.label{font-family:"Crimson Pro",serif;font-weight:600;font-size:11px;letter-spacing:3px;color:var(--accent);text-transform:uppercase}
.btn{position:absolute;background:var(--black);color:var(--white);font-family:"Crimson Pro",serif;font-weight:600;font-size:13px;display:flex;align-items:center;justify-content:center;gap:6px}
.btn svg{width:11px;height:8px}
.btn.is-light{background:var(--white);color:var(--black)}

/* hero */
.hero{left:0;top:0;width:1200px;height:531px;background:radial-gradient(ellipse at 50% 45%,#9a9c9f 0%,#6f7175 45%,#3b3c3f 100%)}
.topbar{left:0;top:0;width:1200px;height:35px;background:rgba(20,20,20,.55)}
.topbar-item{top:10px;color:var(--white);font-size:12.5px;display:flex;align-items:center;gap:5px}
.topbar-item svg{width:10px;height:10px}
.nav-link{top:71px;color:var(--white);font-family:"Crimson Pro",serif;font-weight:600;font-size:13px;letter-spacing:.5px}
.nav-link.is-active{color:var(--accent-light);text-decoration:underline;text-underline-offset:3px}
.brand{left:540px;top:22px;width:120px;height:112px;color:var(--white);font-family:"Playfair Display",serif;font-weight:700;font-size:13px;line-height:1.15;text-align:center;display:flex;flex-direction:column;align-items:center;justify-content:center;gap:6px}
.brand .dot{width:12px;height:12px;border-radius:50%;background:var(--white)}
.search{left:794px;top:66px;width:129px;height:25px;border:1px solid rgba(255,255,255,.7);color:#ddd;font-size:11.5px;padding:5px 9px}
.search .sep{position:absolute;right:25px;top:0;width:1px;height:23px;background:rgba(255,255,255,.7)}
.search svg{position:absolute;right:8px;top:7px;width:9px;height:9px}
.hero-title{left:0;width:1200px;top:184px;text-align:center;color:var(--white);font-size:52px;line-height:50px}
.hero-text{left:0;width:1200px;top:308px;text-align:center;color:var(--white);font-size:14px;line-height:19px}
.mouse{width:11px;height:18px;border:1.5px solid #777;border-radius:6px}

/* about */
.about-rule{left:160px;top:592px;width:40px;height:1px;background:var(--accent)}
.about-title{left:160px;top:608px;font-size:25px;line-height:32px}
.about-text{left:160px;top:690px;width:400px;font-size:13.5px;line-height:17.7px;color:#222}
.call{left:161px;top:779px;font-family:"Playfair Display",serif;font-weight:700;font-size:16px}
.call span{color:var(--accent);font-weight:600}
.about-frame{left:602px;top:614px;width:343px;height:240px;border:1px solid var(--line)}
.about-photo{left:613px;top:590px;width:362px;height:252px;background:linear-gradient(135deg,#9aa0a6,#5d6268 55%,#3f4247)}

/* services */
.services{left:0;top:904px;width:1200px;height:454px;background:radial-gradient(circle at 50% 30%,#3a3a3a,var(--darker) 80%)}
.services .label{position:absolute;left:0;width:1200px;top:60px;text-align:center;color:var(--accent-light)}
.services-title{left:0;width:1200px;top:78px;text-align:center;color:var(--white);font-size:25px}
.card{width:165px;height:265px;top:128px}
.card svg.shape{position:absolute;left:0;top:0}
.card-icon{position:absolute;left:62px;top:38px;width:42px;height:42px}
.card-title{position:absolute;left:0;width:165px;top:88px;text-align:center;color:var(--ink);font-family:"Playfair Display",serif;font-weight:700;font-size:14px;letter-spacing:-.2px}
.card-text{position:absolute;left:10px;width:145px;top:118px;text-align:center;font-size:13px;line-height:17.6px;color:#222}
.card-link{position:absolute;left:0;width:165px;top:199px;text-align:center;font-size:13px;font-weight:600;color:var(--accent)}
.card-link span{border-bottom:1px solid var(--accent)}

/* discount */
.discount{left:0;top:1358px;width:1200px;height:195px;background:var(--dark)}
.discount-title{left:160px;top:72px;font-size:25px;line-height:34px;color:var(--white)}
.discount-title span{color:var(--accent-light)}
.voucher{left:486px;top:32px;width:374px;height:163px;background:linear-gradient(135deg,#f2f2f2 0%,#e0e0e0 40%,#8c8c8c 70%,#4d4d4d 100%);clip-path:polygon(18% 0,60% 0,100% 100%,0 100%,0 70%)}

/* news */
.news{left:0;top:1553px;width:1200px;height:444px;background:var(--light)}
.news-band{left:0;top:231px;width:1200px;height:213px;background:var(--band)}
.news .label{position:absolute;left:0;width:1200px;top:54px;text-align:center}
.news-title{left:0;width:1200px;top:69px;text-align:center;font-size:25px}
.post{top:123px;width:279px}
.post-photo{width:279px;height:190px}
.post-meta{margin-top:14px;display:flex;gap:32px;color:var(--white);font-size:10px}
.post-meta span{display:flex;align-items:center;gap:5px}
.post-meta svg{width:8px;height:8px}
.post-title{margin-top:9px;color:var(--white);font-family:"Playfair Display",serif;font-weight:600;font-size:13.5px;line-height:19.5px}

/* footer */
.footer{left:0;top:1997px;width:1200px;height:506px;background:radial-gradient(circle at 50% 40%,#242424,#0d0d0d 85%)}
.subscribe-title{left:160px;top:34px;font-size:25px;line-height:35px;color:var(--white)}
.subscribe-title span{color:var(--accent-light)}
.subscribe-input{left:571px;top:45px;width:329px;height:38px;background:var(--white);font-size:11.5px;color:#888;padding:12px 19px}
.subscribe-btn{left:900px;top:45px;width:113px;height:38px;background:#5a5a5a}
.footer-brand{left:160px;top:184px;width:108px;height:132px;color:var(--white);font-family:"Playfair Display",serif;font-weight:700;font-size:12.5px;line-height:1.15;text-align:center;display:flex;flex-direction:column;align-items:center;justify-content:center;gap:6px}
.footer-brand .dot{width:12px;height:12px;border-radius:50%;background:var(--white)}
.footer-about{left:160px;top:359px;width:225px;color:var(--white);font-size:12.5px;line-height:16.5px}
.footer-col{top:186px;color:var(--white)}
.footer-col h3{font-family:"Playfair Display",serif;font-weight:700;font-size:15px;margin-bottom:26px}
.footer-col li{list-style:none;font-size:12.5px}
.footer-col li.is-active{color:var(--accent-light);text-decoration:underline}
.company li{margin-bottom:16px}
.service-list li{margin-bottom:12.5px}
.contact li{display:flex;gap:5px;margin-bottom:15px;line-height:14px}
.contact svg{width:10px;height:10px;flex:none;margin-top:2px}
.social{display:flex;gap:4px}
.social i{width:11px;height:11px;border:1px solid var(--white);border-radius:50%}
.copyright{left:0;width:1200px;top:487px;text-align:center;color:var(--white);font-size:12px}
</style>
</head>
<body>

<header class="abs hero" role="img" aria-label="Photo of a pickup truck being sprayed with water at a wash bay">
</header>
<div class="abs topbar"></div>
<div class="abs topbar-item" style="left:161px">
  <svg viewBox="0 0 10 10"><circle cx="5" cy="5" r="4" fill="none" stroke="#c4c4c4" stroke-width="1.3"/><circle cx="5" cy="5" r="1.4" fill="#c4c4c4"/></svg>
  Maple Row, Suite 400 Fairview, ST 10010
</div>
<div class="abs topbar-item" style="left:765px">
  <svg viewBox="0 0 10 10"><circle cx="5" cy="5" r="4" fill="none" stroke="#c4c4c4" stroke-width="1.3"/><path d="M3.5 3.2l1 1-.5.6.9.9.6-.5 1 1-.7.7C4.6 6.7 3.3 5.4 2.9 4z" fill="#c4c4c4"/></svg>
  (+00) 0100 555010
</div>
<div class="abs topbar-item" style="left:910px">
  <svg viewBox="0 0 10 10"><circle cx="5" cy="5" r="4" fill="none" stroke="#c4c4c4" stroke-width="1.3"/><rect x="3" y="3.6" width="4" height="2.8" fill="#c4c4c4"/></svg>
  hello@shorelinedetail.com
</div>

<nav>
  <span class="abs nav-link is-active" style="left:325px">HOME</span>
  <span class="abs nav-link" style="left:397px">SERVICES</span>
  <span class="abs nav-link" style="left:486px">BLOG</span>
  <span class="abs nav-link" style="left:682px">CONTACT US</span>
</nav>
<div class="abs brand"><i class="dot"></i>SHORELINE<br>MOBILE<br>DETAILING</div>
<div class="abs search">Search<i class="sep"></i>
  <svg viewBox="0 0 10 10"><circle cx="4" cy="4" r="3" fill="none" stroke="#fff" stroke-width="1.2"/><path d="M6.3 6.3L9 9" stroke="#fff" stroke-width="1.2"/></svg>
</div>

<h1 class="abs heading hero-title">Interior and Exterior<br>Cleaning</h1>
<p class="abs hero-text">Lorem Ipsum is simply dummy text of the printing and typesetting industry.<br>Lorem Ipsum has been the industry's standard</p>
<a class="btn" style="left:545px;top:374px;width:128px;height:31px">Appointment <svg viewBox="0 0 11 8"><path d="M0 4h10M7 1l3 3-3 3" fill="none" stroke="#fff" stroke-width="1.2"/></svg></a>
<svg class="abs" style="left:440px;top:495px" width="320" height="37" viewBox="0 0 320 37"><path d="M0 37C60 37 80 0 160 0S260 37 320 37z" fill="#fff"/></svg>
<div class="abs mouse" style="left:594px;top:510px"></div>

<section>
  <div class="abs about-rule"></div>
  <p class="abs label" style="left:205px;top:585px">Lorem Ipsum</p>
  <h2 class="abs heading about-title">Professional washing<br>and cleaning of your car &amp; House</h2>
  <p class="abs about-text">Lorem Ipsum is simply dummy text of the printing and typesetting industry. Lorem Ipsum has been the industry's standard dummy text ever since the 1500s, when an unknown printer took a galley of type and scrambled it to make a type specimen book.</p>
  <p class="abs call">Call for book: <span>(+00) 0100 555010</span></p>
  <a class="btn" style="left:161px;top:827px;width:107px;height:31px">know more <svg viewBox="0 0 11 8"><path d="M0 4h10M7 1l3 3-3 3" fill="none" stroke="#fff" stroke-width="1.2"/></svg></a>
  <div class="abs about-frame"></div>
  <div class="abs about-photo" role="img" aria-label="Photo of a worker power washing a metal roof"></div>
</section>

<section class="abs services">
  <p class="label">Our Services</p>
  <h2 class="abs heading services-title">Services We Offers</h2>

  <article class="abs card" style="left:195px">
    <svg class="shape" width="165" height="265" viewBox="0 0 165 265"><path d="M1 28Q82.5-18 164 28V244Q82.5 286 1 244Z" fill="#fff" stroke="#8a8a8a" stroke-width="1.5"/></svg>
    <svg class="card-icon" viewBox="0 0 42 42" fill="none" stroke="#333" stroke-width="1.2"><rect x="16" y="6" width="20" height="26"/><path d="M20 13h12M20 18h12M20 23h12M5 22h10l2 6H3z"/><circle cx="7" cy="30" r="2"/></svg>
    <h3 class="card-title">CAR INSPECTION</h3>
    <p class="card-text">Lorem Ipsum is simply dummy text of the printing and typesetting industry Lorem Ipsum industry</p>
    <p class="card-link"><span>Read More</span></p>
  </article>
  <article class="abs card" style="left:387px">
    <svg class="shape" width="165" height="265" viewBox="0 0 165 265"><path d="M1 28Q82.5-18 164 28V244Q82.5 286 1 244Z" fill="#fff" stroke="#8a8a8a" stroke-width="1.5"/></svg>
    <svg class="card-icon" viewBox="0 0 42 42" fill="none" stroke="#333" stroke-width="1.2"><rect x="13" y="2" width="14" height="14"/><path d="M20 16v6M10 22h20v16H10zM20 22v16M2 39h38"/></svg>
    <h3 class="card-title">AUTO PAINTING</h3>
    <p class="card-text">Lorem Ipsum is simply dummy text of the printing and typesetting industry Lorem Ipsum industry</p>
    <p class="card-link"><span>Read More</span></p>
  </article>
  <article class="abs card" style="left:579px">
    <svg class="shape" width="165" height="265" viewBox="0 0 165 265"><path d="M1 28Q82.5-18 164 28V244Q82.5 286 1 244Z" fill="#fff" stroke="#8a8a8a" stroke-width="1.5"/></svg>
    <svg class="card-icon" viewBox="0 0 42 42" fill="none" stroke="#333" stroke-width="1.2"><circle cx="26" cy="10" r="7"/><path d="M26 6v8M6 28h12l8-6 4 3-8 8H8zM4 30l4 8"/></svg>
    <h3 class="card-title">AUTO FINANCING</h3>
    <p class="card-text">Lorem Ipsum is simply dummy text of the printing and typesetting industry Lorem Ipsum industry</p>
    <p class="card-link"><span>Read More</span></p>
  </article>
  <article class="abs card" style="left:771px">
    <svg class="shape" width="165" height="265" viewBox="0 0 165 265"><path d="M1 28Q82.5-18 164 28V244Q82.5 286 1 244Z" fill="#fff" stroke="#8a8a8a" stroke-width="1.5"/></svg>
    <svg class="card-icon" viewBox="0 0 42 42" fill="none" stroke="#333" stroke-width="1.2"><rect x="16" y="6" width="20" height="26"/><path d="M20 13h12M20 18h12M20 23h12M5 22h10l2 6H3z"/><circle cx="7" cy="30" r="2"/></svg>
    <h3 class="card-title">HEIGHTENED CARE</h3>
    <p class="card-text">Lorem Ipsum is simply dummy text of the printing and typesetting industry Lorem Ipsum industry</p>
    <p class="card-link"><span>Read More</span></p>
  </article>
</section>

<section class="abs discount">
  <div class="abs mouse" style="left:594px;top:2px"></div>
  <h2 class="abs heading discount-title">Hurry to join<br><span>the discount program</span></h2>
  <div class="abs voucher" role="img" aria-label="Illustration of two gift voucher cards with ribbons"></div>
  <a class="btn is-light" style="left:932px;top:85px;width:111px;height:31px">Get a Quite <svg viewBox="0 0 11 8"><path d="M0 4h10M7 1l3 3-3 3" fill="none" stroke="#111" stroke-width="1.2"/></svg></a>
</section>

<section class="abs news">
  <div class="abs news-band"></div>
  <p class="label">News From Blog</p>
  <h2 class="abs heading news-title">Our Latest News</h2>

  <article class="abs post" style="left:160px">
    <div class="post-photo" role="img" aria-label="Photo of a person power washing a garden path" style="background:linear-gradient(160deg,#8a8a8a,#5a5a5a 55%,#9a9a9a)"></div>
    <div class="post-meta"><span><svg viewBox="0 0 8 8" fill="none" stroke="#fff"><circle cx="4" cy="2.5" r="1.8"/><path d="M1 8a3 3 0 016 0"/></svg>Sam Carter</span><span><svg viewBox="0 0 8 8" fill="none" stroke="#fff"><rect x=".5" y="1" width="7" height="6.5"/><path d="M.5 3h7"/></svg>May 26, 2019</span></div>
    <h3 class="post-title">Lorem Ipsum is simply dummy text of the printing and typesetting industry</h3>
  </article>
  <article class="abs post" style="left:461px">
    <div class="post-photo" role="img" aria-label="Photo of clean black leather car seats" style="background:linear-gradient(150deg,#6b6b6b,#2a2a2a 55%,#1a1a1a)"></div>
    <div class="post-meta"><span><svg viewBox="0 0 8 8" fill="none" stroke="#fff"><circle cx="4" cy="2.5" r="1.8"/><path d="M1 8a3 3 0 016 0"/></svg>Sam Carter</span><span><svg viewBox="0 0 8 8" fill="none" stroke="#fff"><rect x=".5" y="1" width="7" height="6.5"/><path d="M.5 3h7"/></svg>May 26, 2019</span></div>
    <h3 class="post-title">Lorem Ipsum is simply dummy text of the printing and typesetting industry</h3>
  </article>
  <article class="abs post" style="left:761px">
    <div class="post-photo" role="img" aria-label="Photo of a freshly washed dark sedan under a canopy" style="background:linear-gradient(170deg,#5e5e5e 0%,#8f8f8f 30%,#393939 65%,#6d6d6d)"></div>
    <div class="post-meta"><span><svg viewBox="0 0 8 8" fill="none" stroke="#fff"><circle cx="4" cy="2.5" r="1.8"/><path d="M1 8a3 3 0 016 0"/></svg>Sam Carter</span><span><svg viewBox="0 0 8 8" fill="none" stroke="#fff"><rect x=".5" y="1" width="7" height="6.5"/><path d="M.5 3h7"/></svg>May 26, 2019</span></div>
    <h3 class="post-title">Lorem Ipsum is simply dummy text of the printing and typesetting industry</h3>
  </article>
</section>

<footer class="abs footer">
  <h2 class="abs heading subscribe-title">Subscribe News<br><span>Letter &amp; Get Company News</span></h2>
  <div class="abs subscribe-input">Enter Your Email Address</div>
  <a class="btn subscribe-btn">Subscribe</a>

  <div class="abs footer-brand"><i class="dot"></i>SHORELINE<br>MOBILE<br>DETAILING</div>
  <p class="abs footer-about">We believe brand interaction is key in commu- nication. Real innovations and a positive customer experience are the heart of successful communication.</p>

  <div class="abs footer-col company" style="left:480px">
    <h3>Company</h3>
    <ul><li class="is-active">Home</li><li>Services</li><li>Blog</li><li>Contact Us</li></ul>
  </div>
  <div class="abs footer-col service-list" style="left:676px">
    <h3>Services</h3>
    <ul><li>Latest Cars</li><li>Featured Car</li><li>Sell Your Car</li><li>Buy a Car</li><li>Strategy</li></ul>
  </div>
  <div class="abs footer-col contact" style="left:872px">
    <h3>Contact us</h3>
    <ul>
      <li><svg viewBox="0 0 10 10"><circle cx="5" cy="5" r="4" fill="none" stroke="#c4c4c4" stroke-width="1.3"/><circle cx="5" cy="5" r="1.4" fill="#c4c4c4"/></svg><span>Maple Row, Suite 400 Fairview,<br>ST 10010</span></li>
      <li><svg viewBox="0 0 10 10"><circle cx="5" cy="5" r="4" fill="none" stroke="#c4c4c4" stroke-width="1.3"/><path d="M3.5 3.2l1 1-.5.6.9.9.6-.5 1 1-.7.7C4.6 6.7 3.3 5.4 2.9 4z" fill="#c4c4c4"/></svg>(+00) 0100 555010</li>
      <li><svg viewBox="0 0 10 10"><circle cx="5" cy="5" r="4" fill="none" stroke="#c4c4c4" stroke-width="1.3"/><rect x="3" y="3.6" width="4" height="2.8" fill="#c4c4c4"/></svg>hello@shorelinedetail.com</li>
      <li class="social"><i></i><i></i><i></i></li>
    </ul>
  </div>
  <p class="abs copyright">Copyright © 2020. All Rights Reserved.</p>
</footer>

</body>
</html>
```